BUSINESS CARDS FOR A HOUSE FLIPPING BUSINESS BY TWO WOMEN. THE COMPANY NAME IS "REVAMP BELLES, LLC"

I WILL SEND A PICTURE THAT I WANT ON THE CARD. IT CAN TAKE UP THE WHOLE CARD WITH PINK WRITING . WE WILL BE FLIPPING HOUSES, SO THE LETTERS COULD POSSIBLY BE IN A FLIPPED FASHION. I AM OPEN TO ALL POSSIBILITIES. I WOULD LIKE "REVAMP BELLES" TO BE EMBOSSED IN A PRETTY PINK DESIGN ON THE FRONT. ON THE BACK, IT NEEDS TO SAY "REVAMP BELLES, LLC" (512)648-2975. I AM ALSO LOOKING FOR A TAG LINE IF POSSIBLE.

Real Estate

MUST USE MY SUBMITTED PHOTO TO COVER, IF POSSIBLE, THE FRONT OF CARD. PRETTY PINK LETTERING FOR "REVAMP BELLES" ON THE FRONT.

Requirements
Must have
• THE SUBMITTED PICTURE. YOU CAN ADD COLOR TO THE LIPS OF THE PIC IF YOU CHOOSE, I AM OPEN TO ALL DESIGN IDEAS
Nice to have
• ON THE BACK OF THE CARD, IT CAN HAVE THE BUSINESS NAME AND PHONE NUMBER LISTED ABOVE. IT CAN ALSO HAVE A PIC OF A HOUSE SINCE WE ARE FLIPPING THEM.
ALSO, MARCIE AND I ARE REAL ESTATE DIVAS WITH A COMBINED 30 YEARS OF EXPERIENCE.

```html
<!DOCTYPE html>
<html lang="en">
<head>
<meta charset="utf-8">
<title>Revamp Belles, LLC — Business Cards</title>
<link rel="stylesheet" href="https://fonts.googleapis.com/css2?family=Montserrat:wght@400;500&display=swap">
<style>
  :root {
    --backdrop: #1c1c1e;
    --card-pink: #ff0aa3;
    --card-pink-light: #ff3bb8;
    --sketch-tone: #f2069a;
    --emboss-dark: rgba(150, 0, 90, 0.55);
    --emboss-light: rgba(255, 140, 210, 0.7);
    --ink-white: #ffffff;
  }
  html, body {
    margin: 0;
    width: 1200px;
    height: 930px;
    overflow: hidden;
    background: var(--backdrop);
  }
  .sheet {
    position: relative;
    width: 1200px;
    height: 930px;
  }
  .card {
    position: absolute;
    left: 250px;
    width: 700px;
    height: 400px;
    border-radius: 26px;
    background: linear-gradient(100deg, var(--card-pink) 0%, var(--card-pink-light) 30%, var(--card-pink) 55%);
    overflow: hidden;
    font-family: "Montserrat", sans-serif;
  }
  .card--back { top: 40px; }
  .card--front { top: 490px; }

  .sketch {
    position: absolute;
    border-radius: 14px;
    background: radial-gradient(ellipse at center, var(--sketch-tone) 0%, var(--card-pink) 80%);
    box-shadow: inset 1px 1px 2px var(--emboss-dark), inset -1px -1px 2px var(--emboss-light);
  }
  .card--back .sketch { left: 220px; top: 60px; width: 260px; height: 200px; }
  .card--front .sketch { left: 370px; top: 30px; width: 300px; height: 320px; }

  .embossed {
    position: absolute;
    margin: 0;
    color: var(--card-pink);
    font-weight: 500;
    letter-spacing: 0.04em;
    text-shadow: -1px -1px 1px var(--emboss-dark), 1px 1px 1px var(--emboss-light);
    white-space: nowrap;
  }
  .card--back .embossed {
    left: 0; right: 0; top: 290px;
    text-align: center;
    font-size: 24px;
  }
  .card--front .embossed {
    left: 48px; top: 80px;
    font-size: 28px;
  }
  .phone {
    position: absolute;
    left: 48px; bottom: 44px;
    margin: 0;
    color: var(--ink-white);
    font-size: 28px;
    font-weight: 500;
    letter-spacing: 0.02em;
  }
</style>
</head>
<body>
  <main class="sheet">
    <section class="card card--back" aria-label="Card back">
      <div class="sketch" role="img" aria-label="Embossed line sketch of the two founders, signed Tessa and Marcie"></div>
      <p class="embossed company-name">REVAMP BELLES, LLC</p>
    </section>

    <section class="card card--front" aria-label="Card front">
      <h1 class="embossed company-name">REVAMP BELLES</h1>
      <div class="sketch" role="img" aria-label="Embossed line sketch of the two founders, signed Tessa and Marcie"></div>
      <p class="phone">(512)648-2975</p>
    </section>
  </main>
</body>
</html>
```